Birchway Swing Studio New Location Postcard

I need a postcard announcing our new location. It is a indoor golf training facility that offers award winner instruction, state-of-the-art technology, and custom club fitting. Whether you are a beginner, an aspiring athlete, or an amateur, Birchway Swing Studio offers personalized programs to help take your game to the next level. Call now to schedule your free tour or to sign up. Limited memberships available.
I would like somewhere are on postcard to say Don't put away your clubs just yet! The course may be closed but Birchway Swing Studio's new indoor location is open!
Industry/Entity Type
Training
Look and feel
Each slider illustrates characteristics of the customer's brand and the style your logo design should communicate.

```html
<!DOCTYPE html>
<html lang="en">
<head>
<meta charset="utf-8">
<title>Birchway Swing Studio – New Location Postcard</title>
<link rel="stylesheet" href="https://fonts.googleapis.com/css2?family=Oswald:wght@500&family=Open+Sans:ital,wght@0,400;0,600;1,700&display=swap">
<style>
  :root {
    --border-light: #d6e9b8;
    --border-dark: #afd27f;
    --card: #f5f8fc;
    --brand-red: #e8413a;
    --accent-green: #8dc63f;
    --text-dark: #4a4f52;
    --art-grey: #c9ccce;
    --art-yellow: #e9ebb5;
  }
  html, body {
    margin: 0;
    padding: 0;
    overflow: hidden;
  }
  .postcard {
    position: relative;
    width: 1200px;
    height: 801px;
    overflow: hidden;
    background: linear-gradient(135deg, var(--border-light) 0%, var(--border-dark) 100%);
    font-family: "Open Sans", sans-serif;
  }
  .postcard__face {
    position: absolute;
    left: 56px;
    top: 56px;
    width: 1090px;
    height: 689px;
    background: var(--card);
  }
  .brand__mark {
    position: absolute;
    left: 97px;
    top: 161px;
    width: 138px;
    height: 138px;
    border: 6px solid var(--brand-red);
    border-radius: 50%;
    box-sizing: border-box;
  }
  .brand__rule {
    position: absolute;
    left: 276px;
    top: 152px;
    width: 3px;
    height: 148px;
    background: var(--brand-red);
  }
  .brand__name {
    position: absolute;
    left: 298px;
    top: 150px;
    margin: 0;
    font-family: "Oswald", sans-serif;
    font-weight: 500;
    color: var(--brand-red);
    line-height: 1;
    text-transform: uppercase;
  }
  .brand__name-main {
    display: block;
    font-size: 52px;
    letter-spacing: 1px;
  }
  .brand__name-sub {
    display: block;
    margin-top: 4px;
    font-size: 22px;
    letter-spacing: 7px;
  }
  .brand__address {
    position: absolute;
    left: 300px;
    top: 248px;
    margin: 0;
    font-style: normal;
    font-size: 19px;
    line-height: 26px;
    color: var(--brand-red);
    text-align: center;
    width: 215px;
  }
  .artwork {
    position: absolute;
    left: 80px;
    top: 379px;
    width: 450px;
    height: 270px;
    border-radius: 6px;
    background: linear-gradient(135deg, var(--art-grey) 0%, var(--art-yellow) 50%, var(--art-grey) 100%);
  }
  .divider {
    position: absolute;
    left: 545px;
    top: 104px;
    width: 2px;
    height: 592px;
    background: var(--accent-green);
  }
  .stamp-box {
    position: absolute;
    left: 999px;
    top: 75px;
  }
  .announcement {
    position: absolute;
    left: 583px;
    top: 228px;
    width: 512px;
  }
  .announcement__kicker {
    margin: 0 0 6px;
    font-size: 15px;
    font-weight: 600;
    letter-spacing: 3px;
    text-transform: uppercase;
    color: var(--accent-green);
  }
  .announcement__headline {
    margin: 0 0 10px;
    font-family: "Oswald", sans-serif;
    font-weight: 500;
    font-size: 32px;
    line-height: 1.15;
    color: var(--brand-red);
  }
  .announcement__body {
    margin: 0;
    font-size: 17px;
    line-height: 25px;
    color: var(--text-dark);
  }
  .address-block {
    position: absolute;
    left: 583px;
    top: 468px;
    width: 512px;
  }
  .address-block__label {
    position: absolute;
    left: 0;
    top: 0;
    font-size: 26px;
    font-weight: 700;
    font-style: italic;
    color: var(--accent-green);
  }
  .address-block__line {
    position: absolute;
    right: 0;
    height: 2px;
    background: var(--accent-green);
  }
  .address-block__line--first { top: 29px; width: 464px; }
  .address-block__line--2 { top: 79px; width: 507px; }
  .address-block__line--3 { top: 130px; width: 507px; }
  .address-block__line--4 { top: 179px; width: 507px; }
</style>
</head>
<body>
<main class="postcard">
  <div class="postcard__face"></div>

  <div class="brand__mark" aria-hidden="true"></div>
  <div class="brand__rule" aria-hidden="true"></div>
  <h1 class="brand__name">
    <span class="brand__name-main">Birchway</span>
    <span class="brand__name-sub">Swing Studio</span>
  </h1>
  <address class="brand__address">218 Larkspur Avenue<br>Fernbrook, XX 40712</address>

  <div class="artwork" role="img" aria-label="Sketched golf bag with clubs, a golf ball on a tee and a blank sign on grass"></div>

  <div class="divider" aria-hidden="true"></div>

  <svg class="stamp-box" width="105" height="133" viewBox="0 0 105 133" aria-hidden="true">
    <rect x="4" y="4" width="97" height="125" fill="none" stroke="#8dc63f" stroke-width="4" stroke-dasharray="6 2" stroke-linejoin="round"/>
  </svg>

  <section class="announcement">
    <p class="announcement__kicker">Now open at our new location</p>
    <h2 class="announcement__headline">Don't put away your clubs just yet!</h2>
    <p class="announcement__body">The course may be closed but Birchway Swing Studio's new indoor location is open!</p>
  </section>

  <section class="address-block" aria-label="Recipient address">
    <span class="address-block__label">To:</span>
    <div class="address-block__line address-block__line--first"></div>
    <div class="address-block__line address-block__line--2"></div>
    <div class="address-block__line address-block__line--3"></div>
    <div class="address-block__line address-block__line--4"></div>
  </section>
</main>
</body>
</html>
```